Still Light needs design for Wordpress

I am a Still Light and I need a Wordpress design to offer my distant healing services on a website. It's like Reiki but I use my own healing modality.
It would be great to have a magical design with beautiful colors like purple, I will upload some images so you get an idea of the feel.
The design should communicate lightness and peacefulness, I like playfulness in the design not too blocky.
Need a complete website design, including navigation bar. I do not have a logo yet.

Target Market(s)

Everyone

Requirements
Nice to have
• Works on mobile devices
Should not have
• Too much of typical spiritual symbols on it.

```html
<!DOCTYPE html>
<html lang="en">
<head>
<meta charset="utf-8">
<title>Still Light — Healing</title>
<link rel="stylesheet" href="https://fonts.googleapis.com/css2?family=Oswald:wght@300;400&family=Pathway+Gothic+One&family=Libre+Baskerville:ital@1&family=Open+Sans:wght@400;600&display=swap">
<style>
:root{
  --header-bg:#ececec;
  --ink:#2b2b2b;
  --muted:#444;
  --plum:#45264a;
  --plum-deep:#2d1a30;
  --plum-dark:#2e1d2f;
  --accent:#5a2a5e;
  --side:#e9e9e9;
  --rule:#d6d6d6;
  --white:#fff;
  --footer-text:#f1e9f2;
  --field:#d9d3dc;
}
*{margin:0;padding:0;box-sizing:border-box}
html,body{width:900px;height:1200px;overflow:hidden}
body{position:relative;background:var(--white);font-family:"Open Sans",Arial,sans-serif;color:var(--ink)}

/* header */
.site-header{position:absolute;left:0;top:0;width:900px;height:83px;background:var(--header-bg)}
.brand{position:absolute;left:124px;top:30px;display:flex;align-items:center;gap:9px;font-family:"Oswald",sans-serif;font-weight:400;font-size:19px;color:var(--plum);letter-spacing:1px}
.brand-dot{width:16px;height:16px;border-radius:50%;background:var(--plum)}
.main-nav{position:absolute;right:124px;top:37px;display:flex;gap:27px;font-family:"Pathway Gothic One",sans-serif;font-size:13px;letter-spacing:.5px;color:#333}

/* hero */
.hero{position:absolute;left:0;top:83px;width:900px;height:299px;background:linear-gradient(160deg,#2b6fc1 0%,#6ea3dc 40%,#dfe9f4 70%,#3d7fce 100%)}
.hero-title{position:absolute;left:136px;top:105px;width:255px;height:34px;background:var(--plum-dark);color:#fff;font-family:"Oswald",sans-serif;font-size:22px;font-weight:400;letter-spacing:.8px;line-height:34px;text-align:center}
.hero-text{position:absolute;left:136px;top:150px;width:252px;height:65px;background:#fff;padding:8px 12px;font-family:"Pathway Gothic One",sans-serif;font-size:11.5px;line-height:16px;color:#333;letter-spacing:.4px;overflow:hidden}
.hero-btn{position:absolute;left:136px;top:225px;width:95px;height:26px;background:var(--plum-dark);color:#fff;font-family:"Open Sans",sans-serif;font-weight:600;font-size:10px;letter-spacing:.6px;line-height:26px;text-align:center}
.hero-arrow{position:absolute;top:140px;width:28px;height:28px;border-radius:50%;background:rgba(255,255,255,.85)}
.hero-arrow svg{display:block;margin:8px auto 0}

/* intro */
.intro-title{position:absolute;left:0;top:402px;width:900px;text-align:center;font-family:"Libre Baskerville",serif;font-style:italic;font-weight:400;font-size:18px;color:var(--accent);letter-spacing:.5px}
.intro-sub{position:absolute;left:0;top:430px;width:900px;text-align:center;font-size:9.5px;color:#444}

/* content */
.side-band{position:absolute;top:488px;width:123px;height:450px;background:var(--side)}
.content{position:absolute;left:123px;top:488px;width:653px;height:450px;background:var(--white)}
.section-label{position:absolute;left:14px;font-family:"Oswald",sans-serif;font-weight:300;font-size:11.5px;letter-spacing:.3px;color:#222}
.section-copy{position:absolute;left:14px;width:140px;font-size:8.3px;line-height:14px;color:#333}
.more-link{position:absolute;right:493px;font-size:9px;color:var(--accent);white-space:nowrap}
.card{position:absolute;width:147px}
.card-image{display:block;width:134px;height:116px;margin-left:6px}
.card-caption{margin-top:16px;text-align:center;font-size:9px;color:#222}
.card-rule{margin-top:10px;height:3px;background:var(--rule)}
.divider{position:absolute;left:14px;top:219px;width:623px;height:1px;background:#e3e3e3}

/* footer */
.site-footer{position:absolute;left:0;top:938px;width:900px;height:220px;background:var(--plum);color:var(--footer-text)}
.footer-col{position:absolute;top:38px}
.footer-heading{font-family:"Oswald",sans-serif;font-weight:400;font-size:12px;letter-spacing:.4px;color:#fff;margin-bottom:16px}
.footer-list{list-style:none;font-size:9.5px;line-height:19px}
.quote{font-size:8.5px;font-style:italic;line-height:13.5px;width:128px}
.quote-by{font-size:8.5px;font-weight:600;margin:4px 0 9px}
.contact-row{display:flex;gap:8px;font-size:9px;line-height:13.5px;margin-bottom:9px}
.contact-row svg{flex:none;margin-top:2px}
.social{display:flex;gap:7px;margin-top:2px}
.social span{width:16px;height:16px;border-radius:50%;background:#fff}
.news-copy{font-size:9px;line-height:14px;width:140px;margin-bottom:10px}
.field{width:119px;height:16px;background:var(--field);font-size:8px;color:#8d8290;padding-left:3px;line-height:16px;margin-bottom:5px}
.submit{width:59px;height:16px;background:#fff;color:var(--plum);font-size:8.5px;font-weight:600;text-align:center;line-height:16px;margin-top:6px;letter-spacing:.5px}
.legal{position:absolute;left:0;top:1158px;width:900px;height:42px;background:var(--plum-deep);color:#e6dbe8;font-size:8.5px;padding:14px 0 0 134px}
</style>
</head>
<body>

<header class="site-header">
  <div class="brand"><span class="brand-dot"></span>Still Light</div>
  <nav class="main-nav"><span>HOME</span><span>ABOUT US</span><span>PRODUCTS</span><span>INSTRUCTORS</span><span>BLOG</span><span>CONTACT US</span></nav>
</header>

<section class="hero" role="img" aria-label="Photo of a father lifting a smiling child onto his shoulders against a bright blue sky with white clouds">
  <div class="hero-arrow" style="left:27px"><svg width="12" height="12" viewBox="0 0 12 12"><path d="M8 1 3 6l5 5" fill="none" stroke="#222" stroke-width="1.6"/></svg></div>
  <div class="hero-arrow" style="left:845px"><svg width="12" height="12" viewBox="0 0 12 12"><path d="M4 1l5 5-5 5" fill="none" stroke="#222" stroke-width="1.6"/></svg></div>
  <div class="hero-title">LOREM IPSUM DOLOR SIT</div>
  <div class="hero-text">SED UT PERSPICIATIS UNDE OMNIS ISTE NATUS ERROR SIT VOLUPTATEM ACCUSANTIUM DOLOREMQUE LAUDANTIUM, TOTAM REM APERIAM, EAQUE IPSA QUAE AB ILLO...</div>
  <div class="hero-btn">READ MORE</div>
</section>

<h1 class="intro-title">Excepteur Sint Occaecat Cupidatat</h1>
<p class="intro-sub">Sed ut perspiciatis unde omnis iste natus error sit voluptatem accusantium doloremque laudantium</p>

<div class="side-band" style="left:0"></div>
<div class="side-band" style="left:776px"></div>

<main class="content">
  <h2 class="section-label" style="top:28px">ABOUT STILL LIGHT</h2>
  <p class="section-copy" style="top:70px">Lorem ipsum dolor sit amet, consectetur adipiscing elit. Proin sed ipsum tortor. Nam aliquam lacinia elementum. Lorem ipsum dolor sit amet, consectetur adipiscing elit.</p>
  <span class="more-link" style="top:155px">Learn More &#8250;</span>

  <div class="card" style="left:177px;top:29px">
    <div class="card-image" role="img" aria-label="Photo of hands giving a calming face massage" style="background:linear-gradient(135deg,#f6e3c8,#e9a25a 60%,#c9712e)"></div>
    <p class="card-caption">Healing Practices</p><div class="card-rule"></div>
  </div>
  <div class="card" style="left:331px;top:29px">
    <div class="card-image" role="img" aria-label="Portrait photo of a healing instructor in a white coat" style="background:linear-gradient(180deg,#f2f0ee,#e6ddd6 60%,#c9b8ae)"></div>
    <p class="card-caption">Visit Healing Instructors</p><div class="card-rule"></div>
  </div>
  <div class="card" style="left:484px;top:29px">
    <div class="card-image" role="img" aria-label="Photo of pink blossom trees by a lake at sunset" style="background:linear-gradient(180deg,#f1b569,#b7a0c9 45%,#c979b8 75%,#3f3150)"></div>
    <p class="card-caption">Still Light Video</p><div class="card-rule"></div>
  </div>

  <div class="divider"></div>

  <h2 class="section-label" style="top:262px">LATEST POSTS</h2>
  <p class="section-copy" style="top:304px">Nam libero tempore, cum soluta nobis est eligendi optio cumque nihil impedit quo minus id quod maxime placeat facere possimus, omnis voluptas assumenda est, omnis dolor repellendus.</p>
  <span class="more-link" style="top:392px">Visit Blog &#8250;</span>

  <div class="card" style="left:177px;top:262px">
    <div class="card-image" role="img" aria-label="Photo of a person meditating in silhouette at sunrise" style="background:linear-gradient(180deg,#1d3f9c,#3a6fd0 50%,#f0d36a 70%,#2a3c7a)"></div>
    <p class="card-caption">Reducing Stress</p><div class="card-rule"></div>
  </div>
  <div class="card" style="left:331px;top:262px">
    <div class="card-image" role="img" aria-label="Photo of red cliffs reflected in a calm lake at dusk" style="background:linear-gradient(180deg,#3f3a8a,#b47ac0 40%,#7a4a45 60%,#2a2350)"></div>
    <p class="card-caption">Deepening spiritual connection</p><div class="card-rule"></div>
  </div>
  <div class="card" style="left:484px;top:262px">
    <div class="card-image" role="img" aria-label="Photo of a woman stretching joyfully in a green meadow" style="background:linear-gradient(180deg,#4e7a1e,#9cc64a 55%,#6a9a2a)"></div>
    <p class="card-caption">Strengthening the Immune</p><div class="card-rule"></div>
  </div>
</main>

<footer class="site-footer">
  <div class="footer-col" style="left:134px">
    <h3 class="footer-heading">Healing Practices</h3>
    <ul class="footer-list"><li>Acupuncture</li><li>Aromatherapy</li><li>Chiropractic</li><li>Healing Touch</li><li>Massage Therapy</li><li>Breathwork</li></ul>
  </div>
  <div class="footer-col" style="left:301px">
    <h3 class="footer-heading">Testimonials</h3>
    <p class="quote">&#8220;&nbsp;At vero eos et accusamus et iusto odio dignissimos ducimus&nbsp;&#8221;</p>
    <p class="quote-by">By Clara Wendt</p>
    <p class="quote">&#8220;&nbsp;Temporibus autem quibus dam et aut officiis debitis aut rerum&nbsp;&#8221;</p>
    <p class="quote-by">By Nora Lindqvist</p>
  </div>
  <div class="footer-col" style="left:467px">
    <h3 class="footer-heading">Contact Us</h3>
    <div class="contact-row"><svg width="10" height="10" viewBox="0 0 10 10"><path d="M1 5 5 1l4 4v4H6V6H4v3H1z" fill="#fff"/></svg><span>Lorem Ipsum Street,<br>Lorem Ipsum</span></div>
    <div class="contact-row"><svg width="10" height="10" viewBox="0 0 10 10"><path d="M2 1h2l1 2-1.2 1a6 6 0 0 0 2.2 2.2L7 5l2 1v2c0 .6-.4 1-1 1A8 8 0 0 1 1 2c0-.6.4-1 1-1z" fill="#fff"/></svg><span style="font-weight:600">555-014-2290</span></div>
    <div class="contact-row"><svg width="10" height="8" viewBox="0 0 10 8"><rect x=".5" y=".5" width="9" height="7" fill="none" stroke="#fff"/><path d="M.5.5 5 4.5 9.5.5" fill="none" stroke="#fff"/></svg><span>info@stilllight.example</span></div>
    <div class="social"><span></span><span></span><span></span><span></span></div>
  </div>
  <div class="footer-col" style="left:633px">
    <h3 class="footer-heading">Newsletter</h3>
    <p class="news-copy">Join Still Light and begin your journey on balanced living.</p>
    <div class="field">Name</div>
    <div class="field">Email</div>
    <div class="submit">SUBMIT</div>
  </div>
</footer>
<div class="legal">&#169; Copyright 2013 still light. All Rights Reserved</div>

</body>
</html>
```